Zelmor Harbor Advisors Website

We are interested in developing a complete website and long term maintenance with the developer we choose through this contest.

Zelmor is a financial consulting company. We will have a website that capitalizes on the initial costs of retaining a client by providing additional services the client needs and tyically spend using 3rd parties.

The primary function of the website will be structured as a sales tool to retain and provide financial services to the client. Also, to provide other services that are integral to starting, building, and growing a business in order to increase creditibility and maintain client loyalty.

Through a combination of in-house "white label" services as well well chosen outside professional services as "affiliates".

The website home page must be a an instant curb-side appeal and representation of our desired extraordinary image. That image is a robust, innovative (zElmor), with a sophistication that creates an instant emotion of excitement and confidence that they have finally found that "needle in the haystack" they have been seeking. The feeling that they are compelled to take action lest they lose our contact information and are doomed to sink to the mediocrity that most business accept through a lack of effort and forsite.
Updates

Reason: Emails were going to the wrong account and I didn't receive any notices of questions or designs being posted.

Target Market(s)

Startup, growth and advancing companies seeking capital and other business services such as website and corporate image design, legal, marketing, asset management, investment and business consulting, etc.

Industry/Entity Type

Financial

Requirements
Must have
• We want to see your creativity
Nice to have
Should not have

```html
<!DOCTYPE html>
<html lang="en">
<head>
<meta charset="utf-8">
<title>Zelmor Harbor Advisors</title>
<link href="https://fonts.googleapis.com/css2?family=Open+Sans:wght@400;600&family=Michroma&display=swap" rel="stylesheet">
<style>
  :root {
    --sky-light: #c9dde3;
    --sky-mid: #7fa6b8;
    --sky-deep: #2f5e7a;
    --frame: #d2d3d5;
    --frame-edge: #e6e7e8;
    --panel: #a8a9ac;
    --panel-dark: #939598;
    --tab: #c7c8ca;
    --text-light: #e4e5e6;
    --text-dark: #58595b;
    --accent-yellow: #d7e021;
    --accent-green: #6cc24a;
    --screen-black: #050505;
    --screen-gray: #3a3a3c;
  }
  * { box-sizing: border-box; margin: 0; padding: 0; }
  html, body { width: 1200px; height: 900px; overflow: hidden; }
  body {
    position: relative;
    font-family: "Open Sans", sans-serif;
    background: var(--sky-mid);
  }
  .backdrop {
    position: absolute; inset: 0;
    background: linear-gradient(135deg, var(--sky-light) 0%, var(--sky-mid) 45%, var(--sky-deep) 100%);
  }
  .site-frame {
    position: absolute; left: 97px; top: 25px; width: 1009px; height: 853px;
    background: var(--frame);
    border: 2px solid var(--frame-edge);
    border-radius: 18px;
    box-shadow: 0 6px 16px rgba(0,0,0,.35);
  }
  .languages {
    position: absolute; left: 40px; top: 17px;
    font-size: 15px; color: var(--text-dark); word-spacing: 4px;
  }
  .search { position: absolute; left: 634px; top: 14px; display: flex; align-items: center; gap: 8px; }
  .search-label { font-size: 16px; letter-spacing: 5px; color: var(--text-dark); }
  .search-field {
    width: 236px; height: 24px; border: 3px solid #9a9b9e; border-radius: 4px; background: #c4c5c7;
  }
  .masthead {
    position: absolute; left: 30px; top: 43px; width: 957px; height: 200px;
    border-radius: 14px 14px 0 0; overflow: hidden;
    background: linear-gradient(100deg, #a9c8d4 0%, #bcd3dc 45%, #8fa9b6 70%, #5b7f93 100%);
  }
  .masthead-faint {
    position: absolute; left: 410px; top: 10px;
    font-size: 120px; font-weight: 600; color: rgba(255,255,255,.22); letter-spacing: 2px;
  }
  .brand { position: absolute; left: 52px; top: 38px; color: #3d3e40; }
  .brand-name { font-size: 82px; font-weight: 600; line-height: 1; letter-spacing: 1px; }
  .brand-sub { font-size: 14px; font-weight: 600; letter-spacing: 8px; margin: 6px 0 0 84px; }
  .nav {
    position: absolute; left: 48px; top: 195px; z-index: 2;
    display: flex; align-items: flex-end; gap: 8px;
  }
  .nav-tab {
    width: 100px; height: 35px; background: var(--tab); border: 2px solid #e0e1e2; border-bottom: none;
    border-radius: 3px 3px 0 0; text-align: center; font-size: 15px; color: var(--text-dark); line-height: 33px;
  }
  .nav-tab.is-active { height: 48px; background: var(--panel); line-height: 38px; }
  .content {
    position: absolute; left: 30px; top: 243px; width: 957px; height: 555px; background: var(--panel);
    border-radius: 0 0 10px 10px;
  }
  .welcome { position: absolute; left: 31px; top: 20px; width: 374px; }
  .welcome-title { font-family: "Michroma", sans-serif; color: var(--accent-yellow); font-size: 18px; font-weight: 400; }
  .welcome-title small { font-size: 12px; }
  .welcome p { color: var(--text-light); font-size: 12.4px; line-height: 16px; margin-top: 10px; }
  .player {
    position: absolute; left: 438px; top: 33px; width: 463px; height: 221px;
    background: var(--screen-black); border-radius: 18px; overflow: hidden;
  }
  .player-sheen { position: absolute; left: 8px; top: 8px; right: 8px; height: 100px;
    background: linear-gradient(#9c9d9f, #0c0c0c); border-radius: 12px 12px 0 0; }
  .player-screen {
    position: absolute; left: 54px; top: 38px; width: 357px; height: 142px;
    background: var(--screen-gray); border: 6px solid #0a0a0a; text-align: center; color: #6b6c6e;
  }
  .player-name { font-size: 40px; font-weight: 600; margin-top: 18px; line-height: 1; }
  .player-sub { font-size: 7px; letter-spacing: 4px; margin-top: 4px; }
  .player-play { display: block; margin: 14px auto 0; }
  .scrollbar {
    position: absolute; left: 921px; top: 35px; width: 17px; height: 505px;
    background: linear-gradient(90deg,#1a1a1a,#000); border-radius: 3px;
  }
  .scroll-thumb { position: absolute; left: 5px; top: 24px; width: 8px; height: 34px; background: var(--accent-green); border-radius: 3px; }
  .news {
    position: absolute; left: 25px; top: 276px; width: 882px; height: 256px;
    background: var(--panel-dark); border-radius: 6px; box-shadow: 0 4px 8px rgba(0,0,0,.3);
  }
  .news-pager { position: absolute; left: 86px; top: 18px; display: flex; gap: 44px; color: var(--accent-yellow); font-size: 14px; }
  .news-pager span { display: flex; align-items: center; gap: 6px; }
  .news-body { position: absolute; left: 29px; top: 52px; width: 332px; color: var(--text-light); font-size: 12.8px; line-height: 16px; }
  .news-body p + p { margin-top: 16px; }
  .read-more { position: absolute; left: 245px; top: 221px; color: var(--accent-yellow); font-size: 15px; word-spacing: 4px; }
  .news-photo {
    position: absolute; left: 419px; top: 7px; width: 458px; height: 242px;
    background: linear-gradient(120deg, #c8dcec 0%, #7ea6cc 40%, #2f5a8a 75%, #14304f 100%);
  }
  .footer {
    position: absolute; left: 37px; top: 814px; width: 940px; display: flex; justify-content: space-between;
    color: var(--text-dark); font-size: 15px;
  }
</style>
</head>
<body>
  <div class="backdrop" role="img" aria-label="Photo of a modern glass office tower against a blue sky"></div>

  <div class="site-frame">
    <div class="languages">English Hindi Spanish</div>
    <div class="search"><span class="search-label">Seacrh:</span><span class="search-field"></span></div>

    <header class="masthead" role="img" aria-label="Photo of a glass office building facade">
      <div class="masthead-faint" aria-hidden="true">zElmor</div>
      <div class="brand">
        <div class="brand-name">zElmor</div>
        <div class="brand-sub">HARBOR ADVISORS</div>
      </div>
    </header>

    <main class="content">
      <section class="welcome">
        <h1 class="welcome-title">WELCOME <small>TO OUR COMPANY</small></h1>
        <p>Lorem ipsum dolor sit amet, consectetur adipisicing elit, sed do eiusmod tempor incididunt ut labore et dolore magna al Voluptate velit esse cillum dolore eu fugiat nulla pariatur. Excepteur sint... occaecat cupidatat non pro.</p>
        <p>Lorem ipsum dolor sit amet, consectetur adipisicing elit, sed do eiusmod tempor incididunt ut labore et dolore magna al Voluptate velit..</p>
        <p>Lorem ipsum dolor sit amet, consectetur adipisicing elit, sed do eiusmod tempor incididunt ut labore et dolore magna al Voluptate velit esse cillum dolore eu fugiat nulla pariatur. Excepteur sint... occaecat cupidatat non pro.</p>
      </section>

      <div class="player">
        <div class="player-sheen"></div>
        <div class="player-screen">
          <div class="player-name">zElmor</div>
          <div class="player-sub">HARBOR ADVISORS</div>
          <svg class="player-play" width="30" height="24" viewBox="0 0 30 24"><polygon points="0,0 30,12 0,24" fill="#6cc24a"/></svg>
        </div>
      </div>

      <div class="scrollbar"><div class="scroll-thumb"></div></div>

      <section class="news">
        <div class="news-pager">
          <span><svg width="18" height="12" viewBox="0 0 18 12"><polygon points="0,6 18,0 18,12" fill="#dcdddf"/></svg>Last New</span>
          <span>Next New<svg width="18" height="12" viewBox="0 0 18 12"><polygon points="18,6 0,0 0,12" fill="#dcdddf"/></svg></span>
        </div>
        <div class="news-body">
          <p>Lorem ipsum dolor sit amet, consectetur adipisicing elit, sed do eiusmod tempor incididunt ut labore et dolore magna aliqua. Ut enim ad minim veniam, quis nostrud exercitation ullamco laboris nisi ut aliquip ex ea commodo consequat.</p>
          <p>Duis aute irure dolor in reprehenderit in voluptate velit esse cillum dolore eu fugiat nulla pariatur. Excepteur sint occaecat cupidatat non proident, sunt in culpa qui officia deserunt mollit anim id est laborum."</p>
        </div>
        <div class="read-more">Read More...</div>
        <div class="news-photo" role="img" aria-label="Photo of a business team meeting around a conference table"></div>
      </section>
    </main>

    <nav class="nav">
      <div class="nav-tab is-active">Home</div>
      <div class="nav-tab">About Us</div>
      <div class="nav-tab">Services</div>
      <div class="nav-tab">Contact Us</div>
    </nav>

    <footer class="footer">
      <span>©2011-2020 zElmor. All rights reserved.</span>
      <span>Lorem ipsum dolor sit amet, consectetur</span>
      <span>Home | About Us | Services | Contact Us</span>
    </footer>
  </div>
</body>
</html>
```